Toll For Safer Streets

We need web design for an anti-gun violence campaign that will urge people to ring bells instead of shooting guns to bring in the New Year and whenever someone is killed by gun violence.
This campaign will raise funds for social agencies that help communities with social issues to help especially youth with no place to turn, play or dream. Also will fund New Gun Laws policies. Should be global in aspect but appealing to United States first.
Find poem by Lord Edmund Halvercombe "Turn Lamps, Pale Lamps" as our theme on google.
This is a start up and nothing else to give. But need something eye catching for appeal of campaign.

Target Market(s)

Universal , more male oriented.

Industry/Entity Type

Gun

Number of Pages Required

1 page

Other font styles liked:
• Designers Can Choose

Requirements
Must have
• Strong imagery and vivid colors and bell of course.
Nice to have
• A stand out design beyond words that hit home. See attached file for website ideas

```html
<!DOCTYPE html>
<html lang="en">
<head>
<meta charset="utf-8">
<title>Toll For Safer Streets</title>
<link href="https://fonts.googleapis.com/css2?family=Cabin:wght@400;500;600&display=swap" rel="stylesheet">
<style>
:root{
  --orange:#f26a1b;
  --orange-deep:#e85d10;
  --dark:#2d2a28;
  --ink:#222;
  --text:#6a6a6a;
  --rule:#e2e2e2;
  --white:#fff;
}
*{margin:0;padding:0;box-sizing:border-box}
html,body{width:781px;height:1200px;overflow:hidden;background:var(--white)}
body{position:relative;font-family:"Cabin",Arial,sans-serif;color:var(--text)}
.abs{position:absolute}

/* header */
.brand{left:92px;top:12px;display:flex;align-items:center;gap:10px}
.brand-dot{width:46px;height:46px;border-radius:50%;background:var(--orange)}
.brand-name{font-size:13.5px;font-weight:500;line-height:14px;color:var(--ink);width:80px}
.search{left:474px;top:18px;width:215px;height:26px;border:1px solid #ddd;background:#fff}
.search span{position:absolute;left:7px;top:7px;font-size:7.5px;color:#888;padding-right:6px;border-right:1px solid #ddd}
.search .btn{position:absolute;right:0;top:0;width:26px;height:24px;background:#f0f0f0;border-left:1px solid #ddd}
.search svg{position:absolute;left:7px;top:5px}

.nav{left:91px;top:74px;height:28px;display:flex;align-items:center;font-size:9.5px;color:var(--ink)}
.nav a{color:inherit;text-decoration:none;padding:0 12px;border-left:1px solid #ccc;line-height:12px}
.nav a:nth-child(2){border-left:none}
.nav a.active{background:var(--orange);color:#fff;height:28px;line-height:28px;padding:0 12px;border:none}
.nav-donate{left:628px;top:74px;width:61px;height:28px;background:var(--orange);color:#fff;font-size:9.5px;display:flex;align-items:center;justify-content:center;gap:5px}
.nav-rule{left:0;top:102px;width:781px;height:3px;background:var(--orange)}

/* hero */
.hero{left:0;top:105px;width:781px;height:316px;background:linear-gradient(180deg,#f0a43a 0%,#e58a22 40%,#b9621a 62%,#3a2414 85%,#1d130c 100%)}
.hero-line{left:69px;height:32px;display:flex;align-items:center;font-size:12px;letter-spacing:-.3px;padding:0 16px;text-transform:uppercase}
.hero-line.dark{background:rgba(40,40,40,.92);color:#fff}
.hero-line.light{background:#fff;color:var(--ink)}
.hero-line.light em{font-style:normal;color:var(--orange)}
.hero-more{left:69px;top:314px;width:80px;height:27px;background:#fff;color:var(--ink);font-size:8px;display:flex;align-items:center;justify-content:center;gap:4px}
.hero-arrow{top:240px;width:20px;height:24px;background:rgba(255,255,255,.25);display:flex;align-items:center;justify-content:center}

/* headings */
.section-title{font-size:15.5px;color:var(--ink);text-transform:uppercase;display:flex;align-items:center;gap:8px}
.section-title em{font-style:normal;color:var(--orange)}
.section-title i{display:block;flex:1;height:3px;border-top:1px solid var(--rule);border-bottom:1px solid var(--rule)}
.copy{font-size:7.2px;line-height:14.5px;color:var(--text)}

/* donation band */
.band{left:0;top:541px;width:781px;height:160px;background:var(--dark)}
.band-shadow{left:91px;top:701px;width:600px;height:24px;background:radial-gradient(ellipse at 50% 0%,rgba(0,0,0,.18),rgba(0,0,0,0) 70%)}
.band-title{left:375px;top:561px;font-size:24px;font-weight:400;color:#fff;letter-spacing:.2px;line-height:28px}
.band-sub{left:374px;top:595px;font-size:11px;color:#8c8782;text-transform:uppercase}
.band-btn{left:375px;top:628px;width:73px;height:32px;background:var(--orange);color:#fff;font-size:11px;display:flex;align-items:center;justify-content:center;box-shadow:0 2px 0 #c44e0c}
.band-note{left:374px;top:669px;font-size:7px;color:#8c8782}

/* cards */
.card-img{top:731px;width:183px;height:94px}
.card-tag{position:absolute;left:0;bottom:0;height:17px;padding:0 16px;background:var(--orange);color:#fff;font-size:9.5px;line-height:17px;text-transform:uppercase}
.card-copy{top:840px;width:180px;text-align:justify}
.card-more{top:910px;width:43px;height:22px;background:var(--dark);color:#fff;font-size:7.5px;display:flex;align-items:center;justify-content:center}

/* blog */
.post-title{left:282px;top:993px;font-size:9.5px;color:var(--ink)}
.post-date{left:282px;top:1012px;font-size:7.5px;font-style:italic;color:#999}
.post-copy{left:281px;top:1030px;width:408px;text-align:justify}
.post-more{left:281px;top:1085px;font-size:7.5px;display:flex;align-items:center;gap:5px}

/* footer */
.footer{left:0;top:1130px;width:781px;height:66px;background:var(--orange)}
.footer-base{left:0;top:1196px;width:781px;height:4px;background:#2a2a2a}
.footer-links{left:93px;top:1147px;font-size:7.8px;color:#fff;display:flex}
.footer-links span{padding:0 6px;border-left:1px solid rgba(255,255,255,.8);line-height:9px}
.footer-links span:first-child{padding-left:0;border-left:none}
.footer-copy{left:93px;top:1167px;font-size:7.8px;color:#fff}
.socials{left:502px;top:1156px;display:flex;gap:16px}
.socials span{width:12px;height:12px;border-radius:50%;background:rgba(255,255,255,.9)}
</style>
</head>
<body>

<header>
  <div class="abs brand">
    <div class="brand-dot"></div>
    <div class="brand-name">Toll For Safer Streets</div>
  </div>
  <div class="abs search">
    <span>Search for</span>
    <div class="btn">
      <svg width="13" height="13" viewBox="0 0 13 13"><circle cx="7.5" cy="5.5" r="4" fill="none" stroke="#aaa" stroke-width="1"/><line x1="4.6" y1="8.4" x2="1.5" y2="11.5" stroke="#aaa" stroke-width="1.2"/></svg>
    </div>
  </div>
  <nav class="abs nav">
    <a class="active">Home</a>
    <a>About Us</a>
    <a>Get Involved</a>
    <a>Donate</a>
    <a>Events</a>
    <a>Blog</a>
    <a>Contact Us</a>
  </nav>
  <div class="abs nav-donate">
    <svg width="10" height="10" viewBox="0 0 10 10"><circle cx="5" cy="5" r="5" fill="#fff"/><path d="M5 2.5v5M2.5 5h5" stroke="#f26a1b" stroke-width="1.4"/></svg>
    Donate
  </div>
  <div class="abs nav-rule"></div>
</header>

<section>
  <div class="abs hero" role="img" aria-label="Sunset over the sea with a white bell tower holding three bells"></div>
  <div class="abs hero-line dark" style="top:207px">Turn Lamps, Pale Lamps,</div>
  <div class="abs hero-line dark" style="top:238px">To the dim street, the drifting fog, the frosty light</div>
  <div class="abs hero-line light" style="top:270px">The year is fading in the night;&nbsp;-&nbsp;<em>Lord Edmund Halvercombe</em></div>
  <div class="abs hero-more">MORE DETAILS
    <svg width="8" height="6" viewBox="0 0 8 6"><path d="M0 3h7M4.5 .5 7 3 4.5 5.5" fill="none" stroke="#222" stroke-width="1"/></svg>
  </div>
  <div class="abs hero-arrow" style="left:0"><svg width="8" height="12" viewBox="0 0 8 12"><path d="M6.5 1 1.5 6l5 5" fill="none" stroke="#fff" stroke-width="2"/></svg></div>
  <div class="abs hero-arrow" style="right:0"><svg width="8" height="12" viewBox="0 0 8 12"><path d="M1.5 1l5 5-5 5" fill="none" stroke="#fff" stroke-width="2"/></svg></div>
</section>

<section>
  <h1 class="abs section-title" style="left:94px;top:444px;width:595px;font-weight:400">Welcome to <em>Toll For Safer Streets</em><i></i></h1>
  <p class="abs copy" style="left:93px;top:475px;width:596px;text-align:justify">Consectetuer adipiscing elit. Aenean commodo ligula eget dolor. Aenean massa. Cum sociis natoque penatibus et magnis dis parturient montes, nascetur ridiculus mus. Donec quam felis, ultricies nec, pellentesque eu, pretium quis, sem. Nulla consequat massa quis enim. Donec pede justo, fringilla vel, aliquet nec, vulputate eget, arcu. In enim justo, rhoncus ut, imperdiet a, venenatis vitae, justo. Nullam dictum felis eu pede mollis pretium.</p>
</section>

<section>
  <div class="abs band"></div>
  <div class="abs" style="left:91px;top:541px;width:241px;height:160px;background:radial-gradient(circle at 50% 45%,#d9b88a,#9a6a3c 55%,#5a3a22 100%)" role="img" aria-label="Glass jar filled with coins and paper money"></div>
  <h2 class="abs band-title">MAKE A DONATION</h2>
  <div class="abs band-sub">You'll help save lives for generations to come</div>
  <div class="abs band-btn">DONATE</div>
  <div class="abs band-note">All your funds goes to New Gun Laws policies Campaign</div>
  <div class="abs band-shadow"></div>
</section>

<section>
  <div class="abs card-img" style="left:91px;background:linear-gradient(135deg,#5b5048,#b9a38c 50%,#3e3631)" role="img" aria-label="Campaign volunteers greeting supporters at a gathering">
    <div class="card-tag">About TFSS</div>
  </div>
  <div class="abs card-img" style="left:297px;background:linear-gradient(180deg,#8aa3b8,#6c7a55 50%,#3c3a38)" role="img" aria-label="Crowd at an outdoor rally holding protest signs">
    <div class="card-tag">Get Involved</div>
  </div>
  <div class="abs card-img" style="left:506px;background:linear-gradient(135deg,#7a6a62,#c9c2bd 55%,#8a9bb4)" role="img" aria-label="Speaker with a microphone addressing a seated audience">
    <div class="card-tag">Latest Event</div>
  </div>

  <p class="abs copy card-copy" style="left:91px">Consectetuer adipiscing elit. Aenean commodo ligula eget dolor. Aenean massa. Cum sociis natoque penatibus et magnis dis parturient montes, nascetur ridiculus mus. Donec quam felis, ultricies nec.</p>
  <p class="abs copy card-copy" style="left:296px">Consectetuer adipiscing elit. Aenean commodo ligula eget dolor. Aenean massa. Cum sociis natoque penatibus et magnis dis parturient montes, nascetur ridiculus mus. Donec quam felis, ultricies nec.</p>
  <p class="abs copy card-copy" style="left:509px">Consectetuer adipiscing elit. Aenean commodo ligula eget dolor. Aenean massa. Cum sociis natoque penatibus et magnis dis parturient montes, nascetur ridiculus mus. Donec quam felis, ultricies nec.</p>

  <div class="abs card-more" style="left:91px">MORE</div>
  <div class="abs card-more" style="left:295px">MORE</div>
  <div class="abs card-more" style="left:510px">MORE</div>
</section>

<section>
  <h2 class="abs section-title" style="left:92px;top:956px;width:597px;font-weight:400">Latest from <em>the blog</em><i></i></h2>
  <div class="abs" style="left:91px;top:996px;width:163px;height:96px;background:linear-gradient(135deg,#6f5a4a,#c98a7a 50%,#d8465a 70%,#4a3e3a)" role="img" aria-label="Volunteer writing on a clipboard in a donation warehouse"></div>
  <div class="abs post-title">Consectetuer adipiscing elit. Aenean commodo ligula eget dolor. Aenean massa.</div>
  <div class="abs post-date">September 22nd, 2014</div>
  <p class="abs copy post-copy">Consectetuer adipiscing elit. Aenean commodo ligula eget dolor. Aenean massa. Cum sociis natoque penatibus et magnis dis parturient montes, nascetur ridiculus mus. Donec quam felis, ultricies nec, pellentesque eu pretium quis, sem. Nulla consequat massa quis enim. Donec pede justo, fringilla vel.</p>
  <div class="abs post-more">
    <svg width="8" height="8" viewBox="0 0 8 8"><circle cx="4" cy="4" r="4" fill="#f26a1b"/><path d="M3 2l2 2-2 2" fill="none" stroke="#fff" stroke-width="1"/></svg>
    Continue Reading
  </div>
</section>

<footer>
  <div class="abs footer"></div>
  <div class="abs footer-links"><span>Home</span><span>About Us</span><span>Get Involved</span><span>Donate</span><span>Events</span><span>Blog</span><span>Contact Us</span></div>
  <div class="abs footer-copy">Copyright © 2014 Privacy policy</div>
  <div class="abs socials"><span></span><span></span><span></span><span></span><span></span><span></span><span></span></div>
  <div class="abs footer-base"></div>
</footer>

</body>
</html>
```